Website Design for Luxury Product

Are you tired of the "same-old-same-old"?
Would you like to make a difference?
Do you want to make your mark as a designer and work on a full and cool project?
If you answered "YES" to any of the questions above ... keep on reading. We've been looking for you!
Our cigar company www.velmorsmokes.com is in need of a new website design.
The look-and-feel needs to ooze luxury, be clean, and exciting.
Our goal is to have people visiting our website walk away and:
1. Understand that we are a high end, luxury cigar company
2. Feel a rapport and excitement with our company
3. Establish credibility
4. Have the visitor want to join our monthly VIP cigar club
Our logo is enclosed below
Frequently Asked Questions:
1. Who Is Your Target Market and What Are Your Demographics?
Our target market is 100% is the US and primarily males between the ages of 33 and 65.
Our target market are successful professionals like investment advisers, bankers, accountants, doctors, and entrepreneurs with a high disposable income.
Our audience has the ability to purchase just about anything they would like but prefer to purchase the highest quality items and don't mind paying a premium for this.
The website must give the visitor confidence that we are the "real thing" and that we are the best-of-the-best.
2. What Will The Website Be Hosted On?
The website will either be hosted as a stand alone website using Control Panel or on a WordPress Site.
3. What Font Should I Use For the Website?
Our standard font is the Gotham Family of Fonts.
4. What Colors Should the Website Use?
Surprise us.
Our goal is to have the website that is modern, hip, cool and oozes luxury.
5. What Look and Feel Should I Use?
Take a look at our newly designed logo which is attached as a file. We are after a look that is modern, clean, and luxurious.
If you think you have the "right stuff" we'd love to hear from you with your design.
Harold and Brian
Target Market(s)
Industry/Entity Type
Social Club
Coding
Coded - Design and coding required
Number of Pages Required
5+ page
Font styles to use
Other font styles liked:
- Gotham Family of Fonts
Requirements
Must have
- My project must have a home page and supporting pages with a consistent them that is
- Modern
- Luxurious
- Establishes Credibility
- For the content to use please look to our website with the existing wording.
Nice to have
- Use your imagination on this one.
Should not have
- Our project should not have a look and feel that is ornate and complicated. An example of this is our existing logo which can be found on our website www.velmorsmokes.com
- We have moved away from this look.

```html
<!DOCTYPE html>
<html lang="en">
<head>
<meta charset="utf-8">
<title>Velmor Smokes — Welcome</title>
<link rel="stylesheet" href="https://fonts.googleapis.com/css2?family=Didact+Gothic&family=Mulish:wght@700&display=swap">
<style>
  :root {
    --page-bg: #e8e8e8;
    --ink: #333333;
    --card-dark: #353535;
    --footer-bg: #333333;
    --muted: #bdbdbd;
    --field-bg: #454545;
    --field-line: #8a8a8a;
    --button-bg: #4b4b4b;
    --white: #ffffff;
    --badge-bg: #dcdcdc;
  }
  * { margin: 0; padding: 0; box-sizing: border-box; }
  html, body { width: 1200px; height: 1200px; overflow: hidden; }
  body {
    position: relative;
    background: var(--page-bg);
    color: var(--ink);
    font-family: "Didact Gothic", "Century Gothic", sans-serif;
  }

  .welcome { position: absolute; left: 94px; top: -8px; }
  .welcome__title { font-size: 44px; font-weight: 400; line-height: 1; letter-spacing: 0.5px; }
  .welcome__text { margin-top: 14px; font-size: 18px; line-height: 22px; }

  .tile {
    position: absolute;
    width: 491px;
    height: 284px;
    display: flex;
    flex-direction: column;
    align-items: center;
    justify-content: center;
    overflow: hidden;
  }
  .tile--vip { left: 91px; top: 135px; background: var(--card-dark); }
  .tile--story { left: 616px; top: 135px; }
  .tile--taste { left: 91px; top: 451px; }
  .tile--blend { left: 617px; top: 451px; }

  .tile__photo { position: absolute; inset: 0; }
  .tile__photo--weave { background: radial-gradient(circle at 45% 45%, #5a5a5a, #3a3a3a 55%, #2a2a2a); }
  .tile__photo--wood { background: radial-gradient(ellipse at 55% 20%, #3d3a33, #6c665b 55%, #8f8a80 80%, #5a564f); }
  .tile__photo--stone { background: radial-gradient(circle at 50% 40%, #5e5e5e, #3b3b3b 60%, #1f1f1f); }

  .tile__title {
    position: relative;
    font-family: "Mulish", "Century Gothic", sans-serif;
    font-weight: 700;
    font-size: 39px;
    color: var(--white);
    text-shadow: 0 2px 4px rgba(0,0,0,0.5);
  }
  .tile--vip .tile__title { text-shadow: none; font-size: 40px; margin-top: -12px; }
  .tile__text {
    margin-top: 12px;
    width: 400px;
    text-align: center;
    font-size: 24px;
    line-height: 28px;
    color: var(--muted);
  }
  .tile__button {
    margin-top: 26px;
    width: 169px;
    height: 33px;
    border: 1px solid #a9a9a9;
    border-radius: 5px;
    color: var(--white);
    font-size: 15px;
    line-height: 31px;
    text-align: center;
  }

  .footer {
    position: absolute;
    left: 0; top: 822px;
    width: 1200px; height: 378px;
    background: var(--footer-bg);
    text-align: center;
    color: var(--muted);
  }
  .footer__badge {
    position: absolute;
    left: 563px; top: 0;
    width: 73px; height: 58px;
    background: var(--badge-bg);
    display: flex; align-items: center; justify-content: center;
    color: var(--ink);
    font-size: 11px;
    letter-spacing: 1px;
  }
  .footer__title { position: absolute; left: 0; right: 0; top: 98px; font-size: 24px; }
  .contact-form__field {
    position: absolute;
    top: 147px;
    width: 197px; height: 38px;
    background: var(--field-bg);
    border: 1px solid var(--field-line);
    color: var(--muted);
    font-size: 19px;
    line-height: 36px;
    text-align: left;
    padding-left: 15px;
  }
  .contact-form__field--name { left: 295px; }
  .contact-form__field--email { left: 500px; }
  .contact-form__field--contact { left: 706px; }
  .contact-form__send {
    position: absolute;
    left: 501px; top: 211px;
    width: 196px; height: 37px;
    background: var(--button-bg);
    border-radius: 6px;
    font-size: 19px;
    line-height: 37px;
  }
  .footer__address { position: absolute; left: 0; right: 0; top: 301px; font-size: 19px; line-height: 23px; }
</style>
</head>
<body>
  <header class="welcome">
    <h1 class="welcome__title">Welcome</h1>
    <p class="welcome__text">Our fellow brothers and sisters of the leaf, welcome ... you've arrived.<br>
    At Velmor Smokes our mission is to elevate your enjoyment of cigars and life's special moments</p>
  </header>

  <section class="tile tile--vip">
    <h2 class="tile__title">VIP Club</h2>
    <p class="tile__text">You Are About To Embark On A Journey Unlike Any You Have Ever Experienced.</p>
    <div class="tile__button">Learn More</div>
  </section>

  <section class="tile tile--story">
    <div class="tile__photo tile__photo--weave" role="img" aria-label="Close-up of dark woven rattan in a spiral pattern"></div>
    <h2 class="tile__title">Our Story</h2>
  </section>

  <section class="tile tile--taste">
    <div class="tile__photo tile__photo--wood" role="img" aria-label="Close-up of cracked weathered wood grain"></div>
    <h2 class="tile__title">Taste Profile</h2>
  </section>

  <section class="tile tile--blend">
    <div class="tile__photo tile__photo--stone" role="img" aria-label="Dark dry stone wall texture"></div>
    <h2 class="tile__title">Carbon Blend</h2>
  </section>

  <footer class="footer">
    <div class="footer__badge">VELMOR</div>
    <h2 class="footer__title">Get In Touch</h2>
    <div class="contact-form__field contact-form__field--name">Name</div>
    <div class="contact-form__field contact-form__field--email">Email</div>
    <div class="contact-form__field contact-form__field--contact">Contact</div>
    <div class="contact-form__send">Send</div>
    <p class="footer__address">123 Street Road, City, Zipcode<br>Tel.+12 3456 7890 &nbsp;|&nbsp; info@velmorsmokes.com</p>
  </footer>
</body>
</html>
```